Simple 3 page web design project

This is a simple 3 or 4 page site that is very straight forward.

I have a furnished apartment to lease, and wish to design a clean 3 or 4 page website to advertise the apartment. I am thinking a clean black background with a nice image of the inside of the apartment in the center of the page.

I have attached a rough mockup I did to show what I was thinking of.

Also, room for a nice title and some text above the large picture. At the bottom or on the side, there should be thumbnails that can be clicked to view other images of the apartment with labels below each one.

A menu "Home", "how to rent", and "contact" should be included, as well as a map of where the apartment is on the last page.

I prefer the project be written in HTML5.

I will provide the address and the pictures when I decide on a provider.
Updates

I have attached a sample website mock up I did in photoshop to give you an idea of what I am looking for.

Target Market(s)

business travelers and families needing temporary homes

Industry/Entity Type

Apartment

Requirements
Must have
• Should be written in HTML5
Must be able to upload and resize images using thumbnails
must have a contact form
must have the address on a google map on one of the pages
Must have normal items to optomize google search, such as title page, title, etc.
Should not have
• No add-in modules that will have to be kept up. The site shold be written in HTML

```html
<!DOCTYPE html>
<html lang="en">
<head>
<meta charset="utf-8">
<title>Bayou Crest Group, LLC Properties – Furnished Executive Apartment</title>
<link rel="stylesheet" href="https://fonts.googleapis.com/css2?family=Roboto+Condensed:wght@400;700&family=Open+Sans:wght@400;600;700&display=swap">
<style>
:root{
  --bg-top:#262626;
  --bg-bottom:#141414;
  --gold:#f5c000;
  --gold-dark:#e0a800;
  --gold-text:#f6c22a;
  --nav-dark:#2c2c2c;
  --nav-darker:#1d1d1d;
  --frame:#3a3a3a;
  --frame-edge:#4a4a4a;
  --caption-bg:rgba(22,18,14,.86);
  --body-text:#d9d9d9;
  --muted:#b5b5b5;
  --dim:#6b6b6b;
  --footer:#1b1b1b;
  --base:#000;
}
*{margin:0;padding:0;box-sizing:border-box}
html,body{width:1200px;height:1124px;overflow:hidden;background:var(--base)}
body{position:relative;font-family:"Open Sans",sans-serif}
.page{position:absolute;left:0;top:0;width:1200px;height:992px;
  background:radial-gradient(ellipse at 50% 20%,#2e2e2e 0%,var(--bg-top) 45%,var(--bg-bottom) 100%)}

.brand{position:absolute;left:17px;top:18px;font-family:"Roboto Condensed",sans-serif}
.brand-name{font-size:40px;font-weight:700;color:var(--gold-text);letter-spacing:.5px;line-height:44px}
.brand-tagline{font-size:21px;font-weight:400;color:var(--muted);letter-spacing:.8px;margin-top:4px}

.main-nav{position:absolute;left:798px;top:28px;display:flex;height:59px;box-shadow:0 3px 6px rgba(0,0,0,.6)}
.main-nav a{display:flex;align-items:center;justify-content:center;height:59px;font-size:18px;font-weight:600;
  color:#fff;text-decoration:none;background:linear-gradient(var(--nav-dark),var(--nav-darker));border-left:1px solid #111}
.main-nav a.is-active{background:linear-gradient(#ffd21a,var(--gold-dark));color:#1a1a1a;border-left:none}
.nav-home{width:110px}.nav-rent{width:154px}.nav-contact{width:122px}

.hero-frame{position:absolute;left:16px;top:112px;width:1171px;height:662px;background:var(--frame);
  border:1px solid var(--frame-edge);border-radius:3px;box-shadow:0 4px 14px rgba(0,0,0,.7)}
.hero-photo{position:absolute;left:12px;top:12px;width:1147px;height:637px;overflow:hidden;
  background:
    linear-gradient(90deg,transparent 0 58%,#c2401c 58% 82%,#d9d2c4 82% 100%),
    linear-gradient(180deg,#9a9288 0%,#6e6258 45%,#a07a46 70%,#e9e4dc 100%)}
.hero-photo .photo-shade{position:absolute;inset:0;
  background:linear-gradient(180deg,rgba(255,255,255,.05),rgba(0,0,0,.15));mix-blend-mode:multiply}
.hero-heading{position:absolute;left:42px;top:-4px;font-family:"Roboto Condensed",sans-serif;font-weight:400;
  font-size:64px;color:var(--gold-text);-webkit-text-stroke:2px #111;paint-order:stroke fill;letter-spacing:-.5px}
.hero-caption{position:absolute;left:0;bottom:0;width:100%;height:122px;background:var(--caption-bg);padding:8px 20px 0 15px}
.caption-title{font-size:22px;font-weight:700;color:var(--gold-text);line-height:30px}
.caption-text{font-size:15.6px;color:var(--body-text);line-height:24px;margin-top:6px;width:1100px}
.read-more{position:absolute;right:20px;bottom:6px;font-size:16px;font-weight:600;color:var(--gold-text);text-decoration:none}

.gallery-rail{position:absolute;left:0;top:867px;width:1200px;height:58px;
  background:linear-gradient(#5a5a5a,#3c3c3c);border-top:1px solid #6a6a6a}
.gallery-arrow{position:absolute;top:867px;width:41px;height:58px;display:flex;align-items:center;justify-content:center}
.gallery-arrow.prev{left:0}.gallery-arrow.next{right:0}
.thumb{position:absolute;top:826px;width:267px;height:142px;background:#2a2a2a;border:1px solid #555;
  box-shadow:0 2px 6px rgba(0,0,0,.6)}
.thumb-img{position:absolute;left:7px;top:7px;right:7px;bottom:7px;border-radius:3px}
.thumb-1{left:43px}.thumb-2{left:327px}.thumb-3{left:612px}.thumb-4{left:896px}
.thumb-1 .thumb-img{background:linear-gradient(90deg,#3a3430 0 55%,#7a2616 55% 100%);filter:brightness(.55)}
.thumb-2 .thumb-img{background:linear-gradient(180deg,#e8e4dc 0%,#cfc7bb 55%,#a9372c 75%,#6a6460 100%)}
.thumb-3 .thumb-img{background:linear-gradient(180deg,#7a5a44 0%,#d8d2c8 40%,#3a3538 75%,#8a6a50 100%)}
.thumb-4 .thumb-img{background:linear-gradient(180deg,#6a4a2a 0%,#b6844a 45%,#2a2420 70%,#d8c4a0 100%)}
.zoom-icon{position:absolute;left:105px;top:50px}

.site-footer{position:absolute;left:0;top:992px;width:1200px;height:82px;background:var(--footer)}
.footer-nav{position:absolute;left:16px;top:14px;font-size:15.5px;color:var(--muted)}
.footer-nav a{color:var(--muted);text-decoration:none}
.footer-nav a.is-active{color:var(--gold-text)}
.footer-nav .sep{color:#555;margin:0 9px}
.social{position:absolute;right:12px;top:14px;display:flex;gap:8px}
.social span{width:30px;height:30px;border-radius:50%;background:#5a5a5a;display:block}
.social span.is-active{background:var(--gold-text)}
.copyright{position:absolute;left:0;top:50px;width:100%;text-align:center;font-size:12.5px;color:var(--dim)}
</style>
</head>
<body>
<div class="page">
  <header>
    <div class="brand">
      <div class="brand-name">BAYOU CREST GROUP, LLC PROPERTIES</div>
      <div class="brand-tagline">FURNISHED EXECUTIVE APARTMENT IN MOBILE, ALABAMA</div>
    </div>
    <nav class="main-nav">
      <a class="nav-home is-active" href="#">Home</a>
      <a class="nav-rent" href="#">How to rent</a>
      <a class="nav-contact" href="#">Contact</a>
    </nav>
  </header>

  <section class="hero-frame">
    <div class="hero-photo" role="img" aria-label="Living room with white sofas, red accent wall, television and open kitchen">
      <div class="photo-shade"></div>
      <h1 class="hero-heading">Lorem ipsum dolor sit amet,</h1>
      <div class="hero-caption">
        <h2 class="caption-title">About the furnished apartment</h2>
        <p class="caption-text">This apartment is both newly renovated and furnished with all Restwell furnture to ensure the most comfortable envirment possible. Located in desireable Mid-Town Mobile, Alabama, the apartment is located only miles from downtown as well as shoping</p>
        <a class="read-more" href="#">Read more &nbsp;»</a>
      </div>
    </div>
  </section>

  <div class="gallery-rail"></div>
  <div class="gallery-arrow prev">
    <svg width="18" height="34" viewBox="0 0 18 34"><path d="M15 2 L3 17 L15 32" fill="none" stroke="#f6c22a" stroke-width="3"/></svg>
  </div>
  <div class="gallery-arrow next">
    <svg width="18" height="34" viewBox="0 0 18 34"><path d="M3 2 L15 17 L3 32" fill="none" stroke="#f6c22a" stroke-width="3"/></svg>
  </div>

  <div class="thumb thumb-1">
    <div class="thumb-img" role="img" aria-label="Living room with red wall and television"></div>
    <svg class="zoom-icon" width="48" height="48" viewBox="0 0 48 48">
      <circle cx="19" cy="19" r="15" fill="none" stroke="#fff" stroke-width="4"/>
      <path d="M30 30 L44 44" stroke="#fff" stroke-width="6" stroke-linecap="round"/>
      <path d="M19 11 V27 M11 19 H27" stroke="#fff" stroke-width="4"/>
    </svg>
  </div>
  <div class="thumb thumb-2"><div class="thumb-img" role="img" aria-label="Bright lounge with red armchairs and glass table"></div></div>
  <div class="thumb thumb-3"><div class="thumb-img" role="img" aria-label="Loft living area with brick wall and dark sofas"></div></div>
  <div class="thumb thumb-4"><div class="thumb-img" role="img" aria-label="Kitchen with island and dining table"></div></div>
</div>

<footer class="site-footer">
  <nav class="footer-nav">
    <a class="is-active" href="#">Home</a><span class="sep">/</span><a href="#">How to rent</a><span class="sep">/</span><a href="#">Contact</a><span class="sep">/</span><a href="#">Map</a>
  </nav>
  <div class="social">
    <span class="is-active"></span><span></span><span></span>
  </div>
  <p class="copyright">© 2023 BAYOU CREST GROUP LLC. All rights reserved.</p>
</footer>
</body>
</html>
```